The Hollowreed Project WEBSITE DESIGN

Hollowreed is a not for profit working in international aid and development. The website needs to be lively not depressing,earthy rather than bling, have a dramatic impact over lightweight. It may be that a black and white with spot colour may be more impacting given the simplicity I want for the site. Hollowreed works in partnership with registered NGOs in Asia and Africa. At any one time it will have about five feature projects. The purpose is for people to be able to find out about the projects, the countries, the partner organisations, people's stories and then give people the opportunity to give their financial and volunteer support.

Target Market(s)

First World Donors
All ages but particularly 25 - 55

Industry/Entity Type

Human Rights

Number of Pages Required

5+ page

Font styles to use
Sans Serif

Requirements
Must have
• Simplicity
• Easy access to giving options
• Highlight stories both video and image + copy (sample in attachments)
• Lots of images over copy
Nice to have
• Interest
• Not boring
• May work in black and white with a spot colour or sepia look
Should not have
• Shiny new look
• Dont know how many pages or if it be coded or uncoded - makes no sense to me

```html
<!DOCTYPE html>
<html lang="en">
<head>
<meta charset="utf-8">
<title>The Hollowreed Project</title>
<link rel="stylesheet" href="https://fonts.googleapis.com/css2?family=Raleway:wght@300;400;500;600;700&display=swap">
<style>
:root{
  --accent:#f2b632;
  --ink:#2d2a26;
  --text:#5a5650;
  --muted:#9a958d;
  --sand:#e7e3dc;
  --paper:#ffffff;
  --field:#f4f2ee;
  --line:#dcd7cf;
  --footer:#3b3731;
  --sepia-deep:#2a241d;
  --sepia-dark:#4d4336;
  --sepia-mid:#857561;
  --sepia-light:#c4b49c;
  --sepia-pale:#e2d6c2;
}
*{box-sizing:border-box;margin:0;padding:0}
html,body{width:1200px;height:5040px;overflow:hidden}
body{font-family:"Raleway",sans-serif;color:var(--text);background:var(--paper)}
section,header,footer{position:relative;width:1200px;overflow:hidden}

/* sepia image areas */
.photo{position:absolute;background:
  radial-gradient(ellipse 40% 35% at 30% 40%,rgba(226,214,194,.75),transparent 70%),
  radial-gradient(ellipse 35% 45% at 75% 60%,rgba(42,36,29,.7),transparent 70%),
  radial-gradient(ellipse 50% 30% at 55% 15%,rgba(196,180,156,.8),transparent 70%),
  linear-gradient(165deg,var(--sepia-light),var(--sepia-mid) 50%,var(--sepia-dark))}
.photo.v2{background:
  radial-gradient(ellipse 30% 40% at 60% 35%,rgba(226,214,194,.8),transparent 70%),
  radial-gradient(ellipse 45% 35% at 20% 75%,rgba(42,36,29,.75),transparent 70%),
  linear-gradient(200deg,var(--sepia-mid),var(--sepia-dark) 60%,var(--sepia-deep))}
.photo.v3{background:
  radial-gradient(ellipse 50% 40% at 70% 30%,rgba(240,232,218,.85),transparent 70%),
  radial-gradient(ellipse 40% 40% at 25% 70%,rgba(77,67,54,.7),transparent 70%),
  linear-gradient(140deg,var(--sepia-pale),var(--sepia-light) 45%,var(--sepia-mid))}
.photo.v4{background:
  radial-gradient(ellipse 25% 35% at 35% 55%,rgba(226,214,194,.7),transparent 70%),
  radial-gradient(ellipse 25% 35% at 68% 50%,rgba(226,214,194,.6),transparent 70%),
  radial-gradient(ellipse 60% 30% at 50% 100%,rgba(42,36,29,.8),transparent 70%),
  linear-gradient(180deg,var(--sepia-dark),var(--sepia-mid) 50%,var(--sepia-dark))}

/* hero */
.hero{height:600px}
.hero .photo{inset:0;background:
  linear-gradient(180deg,rgba(20,16,12,.55),rgba(20,16,12,.2) 45%,rgba(20,16,12,.65)),
  radial-gradient(ellipse 30% 40% at 20% 55%,rgba(226,214,194,.55),transparent 70%),
  radial-gradient(ellipse 25% 35% at 80% 60%,rgba(226,214,194,.45),transparent 70%),
  radial-gradient(ellipse 40% 30% at 50% 20%,rgba(196,180,156,.6),transparent 70%),
  linear-gradient(180deg,var(--sepia-mid),var(--sepia-dark) 60%,var(--sepia-deep))}
.brand{position:absolute;left:120px;top:24px;display:flex;align-items:center;gap:10px;color:#fff;font-weight:600;font-size:15px;letter-spacing:1px}
.brand i{width:28px;height:28px;border-radius:50%;background:var(--accent);display:block}
.nav{position:absolute;right:155px;top:58px;display:flex;gap:34px;list-style:none}
.nav li{color:#fff;font-size:12px;font-weight:600;letter-spacing:1px}
.nav li.active{color:var(--accent)}
.hero-title{position:absolute;left:0;right:0;top:270px;text-align:center;color:#fff;font-weight:400;line-height:1}
.hero-title .l1{display:block;font-size:50px;letter-spacing:2px}
.hero-title .l2{display:block;font-size:30px;margin-top:8px;color:var(--accent);letter-spacing:1px}
.hero-title .l3{display:block;font-size:52px;margin-top:6px;letter-spacing:2px}
.dots{position:absolute;left:0;right:0;display:flex;justify-content:center;gap:8px}
.dots i{width:8px;height:8px;border-radius:50%;background:#fff;opacity:.5;display:block}
.dots i.on{opacity:1}
.hero .dots{top:570px}

/* shared */
.heading{position:absolute;left:0;right:0;text-align:center;color:var(--ink);font-size:36px;font-weight:500;letter-spacing:1px}
.heading::after{content:"";display:block;width:130px;height:3px;background:var(--accent);margin:12px auto 0}
.lead{position:absolute;left:240px;right:240px;text-align:center;font-size:13px;line-height:22px;color:var(--text)}
.btn{position:absolute;left:50%;transform:translateX(-50%);display:flex;align-items:center;gap:8px;background:var(--paper);color:var(--ink);font-size:13px;font-weight:700;padding:12px 22px;border-radius:3px;letter-spacing:.5px}
.btn i{width:14px;height:14px;border-radius:50%;background:var(--ink);display:block}
.btn.dark{background:var(--sand)}

/* about */
.about{height:512px;background:
  radial-gradient(ellipse 60% 40% at 50% 100%,rgba(150,135,112,.45),transparent 70%),
  linear-gradient(180deg,var(--sand) 40%,#cfc6b6)}
.about .heading{top:64px}
.purpose{position:absolute;left:0;right:0;top:144px;text-align:center;color:var(--ink);font-size:14px;font-weight:600;text-decoration:underline}
.about .lead{top:176px;left:270px;right:270px}
.about .btn{top:408px}

/* projects */
.projects{height:600px}
.projects .heading{top:56px}
.project{position:absolute;top:160px;width:256px}
.project .photo{position:relative;height:240px;width:256px}
.project h3{margin-top:20px;font-size:17px;font-weight:600;color:var(--ink)}
.project p{margin-top:8px;font-size:12px;line-height:18px;width:200px}

/* news */
.news{height:628px;background:var(--sand)}
.news .heading{top:56px}
.story{position:absolute;left:160px;top:152px;width:880px;height:336px;background:var(--paper);display:flex}
.story .photo{position:relative;flex:0 0 440px;width:440px;height:336px}
.story-body{padding:30px 34px;flex:1}
.story-body h3{font-size:15px;font-weight:600;color:var(--ink);text-align:center}
.story-body p{margin-top:20px;font-size:13px;line-height:22px}
.news .dots{top:560px}
.news .dots i{background:var(--ink)}

/* gallery */
.gallery{height:1284px}
.gallery .heading{top:48px}
.tile{width:288px;height:260px}
.gallery .btn{top:768px}
.divider{position:absolute;left:160px;right:160px;top:860px;height:1px;background:var(--line)}
.video{left:160px;top:920px;width:880px;height:292px}
.video .play{position:absolute;left:50%;top:50%;width:80px;height:80px;margin:-40px 0 0 -40px}

/* donate */
.donate{height:704px;background:var(--sand)}
.donate .heading{top:64px}
.donate .lead{top:150px;left:260px;right:260px}
.form-card{position:absolute;left:160px;top:236px;width:880px;height:396px;background:var(--paper)}
.field{position:absolute;width:370px;height:52px;border:1px solid var(--line);display:flex;align-items:center;background:var(--paper)}
.field .ico{width:52px;height:50px;background:var(--field);border-right:1px solid var(--line);display:flex;align-items:center;justify-content:center}
.field span{padding-left:16px;font-size:13px;color:var(--muted)}
.form-card .btn{top:314px}

/* contact */
.contact{height:600px}
.contact .heading{top:64px}
.contact .lead{top:140px;left:260px;right:260px}
.contact .field{top:250px}
.field.message{left:210px;top:320px;width:780px;height:120px;align-items:flex-start}
.field.message .ico{height:118px;align-items:flex-start;padding-top:16px}
.field.message span{padding-top:16px}
.contact .btn{top:516px}

/* footer */
.site-footer{height:112px;background:var(--footer)}
.site-footer .brand{top:42px;left:120px}
.copyright{position:absolute;left:0;right:0;top:50px;text-align:center;font-size:11px;color:#a59e93}
.social{position:absolute;right:160px;top:40px;display:flex;gap:22px}
.social i{width:30px;height:30px;display:block;background:#fff;border-radius:3px}
</style>
</head>
<body>

<header class="hero">
  <div class="photo" role="img" aria-label="Sepia group photo of a partner community gathered outdoors with volunteers"></div>
  <div class="brand"><i></i>HOLLOWREED</div>
  <ul class="nav">
    <li class="active">HOME</li><li>ABOUT US</li><li>STORIES</li><li>GALLERY</li><li>DONATE</li><li>CONTACTS</li>
  </ul>
  <h1 class="hero-title"><span class="l1">TOGETHER</span><span class="l2">WE CAN CHANGE MANY</span><span class="l3">LIVES</span></h1>
  <div class="dots"><i class="on"></i><i></i><i></i></div>
</header>

<section class="about">
  <h2 class="heading">ABOUT US</h2>
  <p class="purpose">Purpose</p>
  <p class="lead">We partner with local organisations across Asia and Africa to build lasting change from the ground up. Every project is led by people who live in the communities they serve, and every gift goes toward schools, clean water, small business and health care. We believe in dignity, shared effort and long friendships. Read the stories, meet the partners and see how your support turns into real opportunity for families working hard to shape their own future.</p>
  <div class="btn"><i></i>LEARN MORE</div>
</section>

<section class="projects">
  <h2 class="heading">OUR CURRENT PROJECTS</h2>
  <article class="project" style="left:160px">
    <div class="photo v2" role="img" aria-label="Sepia photo of a women's savings group holding certificates"></div>
    <h3>Lotus Cambodia</h3>
    <p>Women's self-help savings groups offer short loans, run schools and help families grow food.</p>
  </article>
  <article class="project" style="left:472px">
    <div class="photo v3" role="img" aria-label="Sepia photo of a woman at a rural self-help group meeting"></div>
    <h3>Hillside Rwanda</h3>
    <p>Women's self-help groups in rural Rwanda.</p>
  </article>
  <article class="project" style="left:784px">
    <div class="photo" role="img" aria-label="Sepia photo of youth leaders gathered outdoors"></div>
    <h3>Riverbend Kenya</h3>
    <p>Coaching women and youth leaders from around the country.</p>
  </article>
</section>

<section class="news">
  <h2 class="heading">NEWS/STORIES FROM PROJECTS</h2>
  <article class="story">
    <div class="photo v4" role="img" aria-label="Sepia photo of schoolchildren sitting together in a classroom"></div>
    <div class="story-body">
      <h3>Amara's Story</h3>
      <p>Before joining the group, I was a seamstress with no steady work. I didn't know that one small loan could open new doors for my children. I thought the cost was too high, yet the women encouraged me and I kept going. Today I run my own shop and can pay school fees for all four of my kids.</p>
    </div>
  </article>
  <div class="dots"><i class="on"></i><i></i><i></i><i></i></div>
</section>

<section class="gallery">
  <h2 class="heading">GALLERY</h2>
  <div class="tile photo v4" style="left:160px;top:148px" role="img" aria-label="Sepia photo of a crowd of children"></div>
  <div class="tile photo" style="left:456px;top:148px" role="img" aria-label="Sepia photo of a community meeting"></div>
  <div class="tile photo v3" style="left:752px;top:148px" role="img" aria-label="Sepia photo of hands working together"></div>
  <div class="tile photo v3" style="left:160px;top:428px" role="img" aria-label="Sepia photo of women seated at a gathering"></div>
  <div class="tile photo v2" style="left:456px;top:428px" role="img" aria-label="Sepia photo of students in a classroom"></div>
  <div class="tile photo" style="left:752px;top:428px" role="img" aria-label="Sepia photo of a woman standing in a field"></div>
  <div class="btn dark"><i></i>SEE ALL</div>
  <div class="divider"></div>
  <div class="video photo v4" role="img" aria-label="Video still of children in a classroom">
    <svg class="play" viewBox="0 0 80 80"><circle cx="40" cy="40" r="38" fill="rgba(0,0,0,.15)" stroke="#fff" stroke-width="3"/><path d="M32 24 L58 40 L32 56 Z" fill="#fff"/></svg>
  </div>
</section>

<section class="donate">
  <h2 class="heading">DONATE US</h2>
  <p class="lead">Every gift, large or small, reaches our partner projects directly. Choose a one-off donation or give monthly and follow the difference your support makes in each community.</p>
  <form class="form-card">
    <div class="field" style="left:50px;top:42px"><div class="ico"><svg width="18" height="18" viewBox="0 0 18 18"><circle cx="9" cy="5" r="4" fill="#9a958d"/><path d="M1 18c0-5 4-7 8-7s8 2 8 7z" fill="#9a958d"/></svg></div><span>Your Name</span></div>
    <div class="field" style="left:460px;top:42px"><div class="ico"><svg width="20" height="14" viewBox="0 0 20 14"><rect width="20" height="14" rx="2" fill="#9a958d"/><rect y="3" width="20" height="3" fill="#f4f2ee"/></svg></div><span>Card Name</span></div>
    <div class="field" style="left:50px;top:114px"><div class="ico"><svg width="20" height="14" viewBox="0 0 20 14"><rect width="20" height="14" fill="#9a958d"/><path d="M0 0 L10 8 L20 0" fill="none" stroke="#f4f2ee" stroke-width="1.5"/></svg></div><span>Email Id</span></div>
    <div class="field" style="left:460px;top:114px"><div class="ico"><svg width="20" height="14" viewBox="0 0 20 14"><rect width="20" height="14" rx="2" fill="#9a958d"/><rect x="3" y="8" width="8" height="2" fill="#f4f2ee"/></svg></div><span>Card Number</span></div>
    <div class="field" style="left:50px;top:186px"><div class="ico"><svg width="14" height="20" viewBox="0 0 14 20"><path d="M7 0a7 7 0 0 1 7 7c0 5-7 13-7 13S0 12 0 7a7 7 0 0 1 7-7z" fill="#9a958d"/><circle cx="7" cy="7" r="2.5" fill="#f4f2ee"/></svg></div><span>Address</span></div>
    <div class="field" style="left:460px;top:186px"><div class="ico"><svg width="16" height="18" viewBox="0 0 16 18"><rect y="8" width="16" height="10" rx="1" fill="#9a958d"/><path d="M3 8V5a5 5 0 0 1 10 0v3" fill="none" stroke="#9a958d" stroke-width="2"/></svg></div><span>Pin Number</span></div>
    <div class="btn dark"><i></i>DONATE</div>
  </form>
</section>

<section class="contact">
  <h2 class="heading">CONTACT US</h2>
  <p class="lead">Have a question about a project, or want to volunteer with one of our partners? Send us a note below and our small team will reply within a few days.</p>
  <div class="field" style="left:210px"><div class="ico"><svg width="18" height="18" viewBox="0 0 18 18"><circle cx="9" cy="5" r="4" fill="#9a958d"/><path d="M1 18c0-5 4-7 8-7s8 2 8 7z" fill="#9a958d"/></svg></div><span>Your Name</span></div>
  <div class="field" style="left:620px"><div class="ico"><svg width="20" height="14" viewBox="0 0 20 14"><rect width="20" height="14" fill="#9a958d"/><path d="M0 0 L10 8 L20 0" fill="none" stroke="#f4f2ee" stroke-width="1.5"/></svg></div><span>Email id</span></div>
  <div class="field message"><div class="ico"><svg width="18" height="18" viewBox="0 0 18 18"><path d="M2 16 L4 11 L13 2 L16 5 L7 14 Z" fill="#9a958d"/></svg></div><span>Write your comment...</span></div>
  <div class="btn dark"><i></i>SUBMIT</div>
</section>

<footer class="site-footer">
  <div class="brand"><i></i>HOLLOWREED</div>
  <p class="copyright">Copyright 2024 The Hollowreed Project. All rights reserved.</p>
  <div class="social"><i></i><i></i>
    <svg width="30" height="30" viewBox="0 0 30 30"><rect y="6" width="30" height="20" fill="#fff"/><path d="M0 6 L15 17 L30 6" fill="none" stroke="#3b3731" stroke-width="2"/></svg>
  </div>
</footer>

</body>
</html>
```